Professional and creatice Life Coach - Business Card design

I just relaunched my website and now i a need a correspoonding business card for my task as life coach. My website is www.tbalrond.com as reference. The compass is kind of a symbol for my work, as I help people navigate through their challenging phases in life. The business card should be colorful, but not too playful as I also adress business people. So it sould be creative, but professional (also to suport my other business as Management Consultant)

Target Market(s)

People who want to get teir problems resolved, in business, partnership and other personal realms

Industry/Entity Type

Life Coaching

Contact Information for Business Card

Front side should include Name, Phone number, Email, Website and address

Font styles to use
Sans Serif

Colors
add136

Requirements
Must have
• "Mag. Leopold Brantner" -> Name
"Energetische Praxis" -> Jobtitle (describing my profession as life coach)
colours and style should match my website www.tbalrond.com
Nice to have
• a compass as a symbol

```html
<!DOCTYPE html>
<html lang="de">
<head>
<meta charset="utf-8">
<title>Leopold Brantner – Visitenkarte</title>
<link href="https://fonts.googleapis.com/css2?family=Arimo:wght@400;600&family=Questrial&display=swap" rel="stylesheet">
<style>
  :root {
    --page-bg: #f1f1f0;
    --card-bg: #ffffff;
    --lime: #b6d163;
    --lime-deep: #a5c63a;
    --ink: #221f1d;
    --text: #3a3a3a;
    --white: #ffffff;
  }
  html, body {
    margin: 0;
    padding: 0;
    width: 1200px;
    height: 1192px;
    overflow: hidden;
    background: var(--page-bg);
  }
  .canvas {
    position: relative;
    width: 1200px;
    height: 1192px;
  }
  .card {
    position: absolute;
    left: 243px;
    width: 714px;
    height: 408px;
    background: var(--card-bg);
    box-shadow: 0 10px 28px rgba(0,0,0,0.18);
  }
  .card--front { top: 88px; }
  .card--back { top: 683px; }
  .card svg { display: block; width: 100%; height: 100%; }
  .fill-lime { fill: var(--lime); }
  .fill-lime-deep { fill: var(--lime-deep); }
  .fill-ink { fill: var(--ink); }
  .greeting {
    font-family: "Arimo", Arial, sans-serif;
    font-size: 36px;
    fill: var(--white);
    letter-spacing: 0.5px;
  }
  .brand-name {
    font-family: "Arimo", Arial, sans-serif;
    font-weight: 600;
    font-size: 40px;
    fill: var(--ink);
  }
  .brand-dot { fill: none; stroke: var(--ink); stroke-width: 4; }
  .person-name {
    font-family: "Arimo", Arial, sans-serif;
    font-weight: 600;
    font-size: 29px;
    fill: var(--ink);
  }
  .job-title {
    font-family: "Arimo", Arial, sans-serif;
    font-size: 24px;
    letter-spacing: 4px;
    fill: var(--ink);
  }
  .contact {
    font-family: "Questrial", "Century Gothic", sans-serif;
    font-size: 25px;
    fill: var(--text);
  }
  .icon-ring { fill: none; stroke: var(--text); stroke-width: 2.6; }
  .icon-glyph { fill: var(--text); }
  .icon-line { fill: none; stroke: var(--text); stroke-width: 2.4; stroke-linejoin: round; }
</style>
</head>
<body>
<main class="canvas">

  <section class="card card--front" aria-label="Vorderseite">
    <svg viewBox="0 0 1050 600" xmlns="http://www.w3.org/2000/svg">
      <g class="brand-mark">
        <circle class="brand-dot" cx="352" cy="205" r="14"/>
        <text class="brand-name" x="380" y="219">Leopold Brantner</text>
      </g>
      <polygon class="fill-lime" points="0,266 256,516 0,516"/>
      <polygon class="fill-lime" points="1050,276 806,516 1050,516"/>
      <polygon class="fill-lime-deep" points="209,471 299,471 256,516"/>
      <polygon class="fill-lime-deep" points="763,471 853,471 806,516"/>
      <polygon class="fill-ink" points="129,392 931,392 853,471 209,471"/>
      <text class="greeting" x="525" y="444" text-anchor="middle">Herzlich Willkommen!</text>
    </svg>
  </section>

  <section class="card card--back" aria-label="Rückseite">
    <svg viewBox="0 0 1050 600" xmlns="http://www.w3.org/2000/svg">
      <text class="person-name" x="75" y="152">Mag. Leopold Brantner</text>
      <text class="job-title" x="75" y="190">Energetische Praxis</text>
      <rect class="fill-lime-deep" x="73" y="212" width="57" height="6"/>
      <rect class="fill-ink" x="130" y="214" width="270" height="3"/>

      <polygon class="fill-ink" points="0,336 485,336 368,452 0,452"/>
      <polygon class="fill-lime" points="655,168 1050,168 1050,526 293,526"/>
      <polygon class="fill-lime-deep" points="219,452 368,452 293,526"/>

      <g class="contact-list">
        <text class="contact" x="955" y="313" text-anchor="end">Birkenweg 14, 5412 Puch, Österreich</text>
        <text class="contact" x="955" y="367" text-anchor="end">+43 660 5550182</text>
        <text class="contact" x="955" y="415" text-anchor="end">leopold@brantner.one</text>
        <text class="contact" x="955" y="468" text-anchor="end">www.tbalrond.com</text>
      </g>

      <g class="contact-icons">
        <circle class="icon-ring" cx="986" cy="305" r="18"/>
        <path class="icon-line" d="M986 316 C980 309 977 304 977 300 A9 9 0 0 1 995 300 C995 304 992 309 986 316 Z"/>
        <circle class="icon-glyph" cx="986" cy="300" r="3"/>

        <circle class="icon-ring" cx="986" cy="357" r="18"/>
        <path class="icon-glyph" d="M979 349 l4 -2 3 6 -3 2 c1 3 3 5 6 6 l2 -3 6 3 -2 4 c-9 1 -17 -7 -16 -16 z"/>

        <circle class="icon-ring" cx="986" cy="407" r="18"/>
        <rect class="icon-glyph" x="977" y="401" width="18" height="12" rx="1.5"/>
        <path d="M977 402 L986 409 L995 402" fill="none" stroke="#b6d163" stroke-width="1.6"/>

        <circle class="icon-ring" cx="986" cy="458" r="18"/>
        <path class="icon-glyph" d="M981 448 L993 459 L987 460 L990 467 L987 468 L984 461 L981 465 Z"/>
      </g>
    </svg>
  </section>

</main>
</body>
</html>
```